High-End audio shop owner needs a business card

I need a personal Business Card for my Audio shop which exists since 1962. We offer high Quality brands, professional Attention and run our own repair-service-department. I look for a design which will be printed on high Quality paper and shall convey trust to the Client that we are very serious. Language is german.

```html
<!DOCTYPE html>
<html lang="de">
<head>
<meta charset="utf-8">
<title>Hi-Fi Klangwerk – Visitenkarte</title>
<link href="https://fonts.googleapis.com/css2?family=Open+Sans:wght@400;700;800&display=swap" rel="stylesheet">
<style>
  :root {
    --stage: #2e2f31;
    --card-white: #ffffff;
    --card-grey: #8e9590;
    --card-grey-light: #a3a9a5;
    --brand-orange: #e8772e;
    --ink-grey: #6b6e70;
    --rule-grey: #8a8d8f;
    --swoosh-grey: #8c918f;
  }
  * { box-sizing: border-box; margin: 0; padding: 0; }
  html, body {
    width: 1200px; height: 900px; overflow: hidden;
    background: var(--stage);
    font-family: "Open Sans", Arial, sans-serif;
  }
  .card {
    position: absolute;
    left: 285px;
    width: 630px; height: 360px;
    overflow: hidden;
    border-radius: 2px;
  }
  .card--back {
    top: 70px;
    background: linear-gradient(135deg, var(--card-grey-light), var(--card-grey));
    display: flex; align-items: center; justify-content: center;
  }
  .card--front { top: 470px; background: var(--card-white); }

  .wordmark {
    display: flex; align-items: center; gap: 10px;
    color: var(--brand-orange);
    font-weight: 800;
    letter-spacing: 0.5px;
    white-space: nowrap;
  }
  .wordmark__square {
    width: 0.6em; height: 0.6em;
    background: var(--brand-orange);
  }
  .card--back .wordmark { font-size: 46px; }
  .card--front .wordmark {
    position: absolute; left: 62px; top: 158px;
    font-size: 26px;
  }

  .divider {
    position: absolute; left: 352px; top: 70px;
    width: 1.5px; height: 130px;
    background: var(--rule-grey);
  }
  .contact {
    position: absolute; left: 372px; top: 66px;
    color: var(--ink-grey);
  }
  .contact__name {
    color: var(--brand-orange);
    font-weight: 700; font-size: 21px; line-height: 1.1;
  }
  .contact__title { font-size: 15px; margin-bottom: 12px; }
  .contact__list { list-style: none; font-size: 14.5px; line-height: 1.55; }
  .contact__list li { display: flex; align-items: center; gap: 10px; }
  .contact__list svg { width: 14px; height: 14px; fill: var(--brand-orange); flex: none; }

  .waves { position: absolute; left: 0; top: 0; width: 630px; height: 360px; }
  .address {
    position: absolute; right: 22px; top: 232px;
    color: var(--card-white);
    font-size: 15px; line-height: 1.35; text-align: right;
  }
</style>
</head>
<body>

<section class="card card--back" aria-label="Kartenrückseite">
  <div class="wordmark"><span class="wordmark__square"></span>Hi-Fi Klangwerk</div>
</section>

<section class="card card--front" aria-label="Kartenvorderseite">
  <svg class="waves" viewBox="0 0 630 360" aria-hidden="true">
    <path fill="var(--brand-orange)" d="M0,360 L0,342 C150,346 300,322 420,262 C500,222 570,200 630,194 L630,360 Z"/>
    <path fill="var(--swoosh-grey)" d="M0,314 C170,328 330,298 460,236 C505,214 540,203 565,198 C525,214 485,240 435,270 C325,328 165,342 0,332 Z"/>
  </svg>

  <div class="wordmark"><span class="wordmark__square"></span>Hi-Fi Klangwerk</div>

  <div class="divider"></div>

  <div class="contact">
    <p class="contact__name">YOUR NAME</p>
    <p class="contact__title">Your Title</p>
    <ul class="contact__list">
      <li><svg viewBox="0 0 24 24"><path d="M6.6 10.8a15.1 15.1 0 0 0 6.6 6.6l2.2-2.2a1 1 0 0 1 1-.25 11.4 11.4 0 0 0 3.6.57 1 1 0 0 1 1 1V20a1 1 0 0 1-1 1A17 17 0 0 1 3 4a1 1 0 0 1 1-1h3.5a1 1 0 0 1 1 1c0 1.25.2 2.45.57 3.57a1 1 0 0 1-.25 1z"/></svg>123-456-2100</li>
      <li><svg viewBox="0 0 24 24"><path d="M2 5h20v14H2z M2 5l10 8 10-8" /></svg>youremail@example.com</li>
      <li><svg viewBox="0 0 24 24"><circle cx="12" cy="12" r="10"/></svg>www.yourwebsite.com</li>
    </ul>
  </div>

  <p class="address">Your address here<br>City, state</p>
</section>

</body>
</html>
```